Bluestone Advisory & Mgmt - Professional Business Cards

Hi!

I am a Real Estate Developer and Construction Consultant.

I have a lot of inspiration from previous designs and would be open to using the attached Designs as a starting point. I would like to see these styles incorporated into your designs.

I really need professional business card to go with it that includes my important info.

Look forward to seeing your designs!.

Target Market(s)

My Target market are building owners, lawyers, consultants.

Industry/Entity Type

Real Estate Development

Contact Information for Business Card

My Name: Dorian Pelkey
My Title: Principle
Company Name: Bluestone Advisory & Mgmt, LLC
Address: 348 West 71st Street, 9th FL New York, NY 10010
Mobile: 917.806.3971
Website: bam-hvx.example

Font styles to use
Serif
Sans Serif

Colors

Designer to choose colors to be used in the design.

Requirements
Must have
• Must incorporate the logo attached or have new that looks similar.
• Must use professional font that will be seen and judged by wealthy land owners and developers.
• Must incorporate some of the color green.
Should not have
• Photo's or pictures of people or buildings of any kind.

```html
<!DOCTYPE html>
<html lang="en">
<head>
<meta charset="utf-8">
<title>Bluestone Advisory &amp; Mgmt – Business Cards</title>
<link href="https://fonts.googleapis.com/css2?family=Lato:wght@400;700&family=Montserrat:wght@600;700&display=swap" rel="stylesheet">
<style>
  :root{
    --backdrop:#36302c;
    --card:#0e0e0e;
    --card-edge:#1b1b1b;
    --green:#3fbf7a;
    --grey:#a19b98;
    --silver:#d4d4d4;
    --text-light:#c9c9c9;
    --divider:#2a2a2a;
  }
  *{margin:0;padding:0;box-sizing:border-box}
  html,body{width:1200px;height:844px;overflow:hidden}
  body{
    background:var(--backdrop);
    font-family:'Lato',Arial,sans-serif;
    position:relative;
  }
  .card{
    position:absolute;
    width:500px;height:286px;
    background:var(--card);
    border:1px solid var(--card-edge);
    box-shadow:0 10px 30px rgba(0,0,0,.45);
  }
  .card--front{left:70px;top:279px}
  .card--back{left:630px;top:279px}

  /* front */
  .brand{
    position:absolute;left:34px;top:96px;width:190px;
  }
  .brand__mark{display:flex;align-items:center;gap:10px}
  .brand__dot{width:18px;height:18px;border-radius:50%;background:var(--green);flex:none}
  .brand__name{
    font-family:'Montserrat',Arial,sans-serif;font-weight:700;
    font-size:30px;color:var(--green);letter-spacing:-.5px;line-height:1;
  }
  .brand__tagline{
    margin-top:10px;font-family:'Montserrat',Arial,sans-serif;font-weight:600;
    font-size:13px;color:var(--green);line-height:1.2;
  }
  .divider{
    position:absolute;left:246px;top:40px;width:1px;height:206px;
    background:var(--divider);
  }
  .contact{position:absolute;left:268px;top:58px;right:20px;color:var(--text-light)}
  .contact__name{font-weight:700;font-size:19px;color:var(--green);line-height:1.1}
  .contact__title{font-size:12px;color:var(--text-light);margin-bottom:10px}
  .contact__line{display:flex;align-items:center;gap:6px;font-size:12.5px;line-height:1.45}
  .contact__line svg{width:11px;height:11px;flex:none}
  .contact__company{margin-top:12px;font-size:12.5px;color:var(--green);line-height:1.35}
  .contact__address{font-size:12.5px;line-height:1.35}

  /* back */
  .card--back .back-name{
    position:absolute;inset:0;display:flex;align-items:center;justify-content:center;
    font-family:'Montserrat',Arial,sans-serif;font-weight:700;
    font-size:52px;color:var(--silver);letter-spacing:-1px;
  }
</style>
</head>
<body>
  <section class="card card--front">
    <div class="brand">
      <div class="brand__mark">
        <span class="brand__dot"></span>
        <span class="brand__name">Bluestone</span>
      </div>
      <div class="brand__tagline">Advisory &amp; Management</div>
    </div>
    <div class="divider"></div>
    <div class="contact">
      <p class="contact__name">Dorian Pelkey</p>
      <p class="contact__title">Principle</p>
      <p class="contact__line">
        <svg viewBox="0 0 12 12" aria-hidden="true"><path fill="var(--text-light)" d="M2.5 1h2l1 2.5-1.3 1a6 6 0 0 0 3.3 3.3l1-1.3L11 7.5v2c0 .8-.7 1.5-1.5 1.5A8.5 8.5 0 0 1 1 2.5C1 1.7 1.7 1 2.5 1z"/></svg>
        917.806.3971
      </p>
      <p class="contact__line">
        <svg viewBox="0 0 12 12" aria-hidden="true"><circle cx="6" cy="6" r="5" fill="none" stroke="var(--text-light)" stroke-width="1.2"/><path d="M1 6h10M6 1c2 2 2 8 0 10M6 1c-2 2-2 8 0 10" fill="none" stroke="var(--text-light)" stroke-width=".9"/></svg>
        www.bam-hvx.example
      </p>
      <p class="contact__company">Bluestone Advisory &amp; Mgmt, LLC</p>
      <p class="contact__address">348 West 71st Street<br>9th FL New York, NY 10010</p>
    </div>
  </section>

  <section class="card card--back">
    <div class="back-name">Bluestone</div>
  </section>
</body>
</html>
```